Business Postcard Mailer - 2 sided - 6 x 10.5 inches

We will be purchasing multiple designs through this project. We need a postcard mailer for a residential painting business. The final design needs to have the special 15% Off, contact information, company logo, stamp indicia, and list of services. I will provide past examples and any additional logos. Company colors are #34482E and #4A1717. Old samples are provided. Final flat size should be 6 x 10.5 inches. And we will need a return address in the upper left-hand corner of the backside. QMRB Layout Guidelines are attached. 4389 Juniper Ave #7, Waukesha, WI 53947.
Updates

I just guaranteed the project and will be expecting more entries. We will also be purchasing additional designs (4-5) so we want to ensure a good variety.

Target Market(s)

Homeowners

Industry/Entity Type

Painting

Font styles to use
Sans Serif

Requirements
Must have
• Logo and brand colors
Nice to have
• Call to action - Book your free estimate at www.BrightCoatCrew.example or Call now 262-555-0147.

```html
<!DOCTYPE html>
<html lang="en">
<head>
<meta charset="utf-8">
<title>BrightCoat Crew Postcard Mailer</title>
<link rel="stylesheet" href="https://fonts.googleapis.com/css2?family=Montserrat:wght@400;500;600;700&family=Roboto+Slab:wght@500;700&display=swap">
<style>
:root{
  --green:#34482e;
  --green-dark:#2a3b25;
  --maroon:#4a1717;
  --paper:#ffffff;
  --backdrop:#e3e3e3;
  --rule:#c9c9c9;
  --muted:#555555;
  --badge:#a9a9a9;
}
*{box-sizing:border-box;margin:0;padding:0}
html,body{width:1200px;height:903px;overflow:hidden}
body{background:var(--backdrop);font-family:"Montserrat",sans-serif;position:relative}
.card{position:absolute;width:689px;height:393px;background:var(--paper);box-shadow:0 2px 6px rgba(0,0,0,.18);overflow:hidden}
.front{left:136px;top:48px}
.back{left:425px;top:462px}
.abs{position:absolute}
.nowrap{white-space:nowrap}
.brand{display:flex;align-items:center;gap:8px;font-weight:700;color:var(--green);letter-spacing:-.5px;white-space:nowrap}
.brand-mark{width:14px;height:14px;background:var(--green);flex:none}
.services{background:linear-gradient(135deg,#3a5233,#2a3b25);color:#fff;list-style:none;padding:14px 0 0 16px;font-size:11.5px;font-weight:500}
.services li{display:flex;align-items:center;gap:8px;margin-bottom:6.5px;white-space:nowrap}
.dot{width:7px;height:7px;border-radius:50%;background:#b9c2b4;flex:none}
.photo{background:linear-gradient(160deg,#d9cdb8,#8b7d6c 55%,#4d4a48)}
.photo-house{background:linear-gradient(180deg,#8fb0c9 0%,#7e9a6a 45%,#3f4c6e 60%,#4f7a3a 100%)}
.caption{background:#fff;color:#333;font-size:11px;text-align:center;line-height:16px;border:1px solid #888;white-space:nowrap}
.specials{display:flex;gap:4px}
.special{flex:1;border:1px solid var(--rule);text-align:center;padding-top:10px;white-space:nowrap}
.special h3{font-family:"Roboto Slab",serif;font-weight:500;color:var(--green);font-size:22px;line-height:1.2}
.special .off{font-family:"Roboto Slab",serif;font-weight:700;color:var(--maroon);font-size:21px;line-height:1.4}
.special .terms{font-family:"Roboto Slab",serif;color:#222;font-size:10px;margin-top:6px}
.or{width:30px;height:30px;border-radius:50%;background:var(--maroon);color:#fff;font-family:"Roboto Slab",serif;font-weight:700;font-size:14px;display:flex;align-items:center;justify-content:center;border:2px solid #fff}
.callbar{background:var(--maroon);color:#fff;font-size:8.5px;font-weight:500;display:flex;align-items:center;gap:5px;padding-left:7px;white-space:nowrap;overflow:hidden}
.callbar svg{width:8px;height:8px;flex:none}
.callbar .lead{font-size:10px}
.callbar .phone{font-size:10px;font-weight:600}
/* back side */
.back-left{left:0;top:0;width:327px;height:393px;border-right:3px solid var(--maroon)}
.mini .special{padding-top:6px}
.mini .special h3{font-size:13.5px}
.mini .special .off{font-size:15px;line-height:1.2}
.mini .special .terms{font-size:7px;margin-top:3px}
.mini-or{width:22px;height:22px;font-size:10px}
.estimates{background:var(--green);color:#fff;padding:8px 0 0 15px}
.estimates h2{font-family:"Roboto Slab",serif;font-weight:500;font-size:17px;margin-bottom:6px}
.estimates ul{list-style:none;display:grid;grid-template-columns:147px 1fr;row-gap:4px;font-size:11.5px;font-weight:500}
.estimates li{display:flex;align-items:center;gap:8px;white-space:nowrap}
.estimates li:nth-child(4){grid-column:2;grid-row:1}
.estimates li:nth-child(5){grid-column:2;grid-row:2}
.ba{overflow:hidden}
.photo-before{background:linear-gradient(180deg,#9fb3c9 0%,#d8d8d4 45%,#7d8a74 100%)}
.photo-after{background:linear-gradient(180deg,#aec3d6 0%,#46546a 45%,#5f7f4a 100%)}
.ribbon{position:absolute;left:-26px;top:10px;width:100px;transform:rotate(-38deg);background:var(--maroon);color:#fff;font-size:9.5px;text-align:center;line-height:15px}
.blurb{font-size:11px;color:var(--muted);line-height:1.3}
.backbar{left:0;top:336px;width:324px;height:57px;background:var(--maroon);color:#fff;overflow:hidden}
.backbar .row1{display:flex;align-items:center;height:25px;white-space:nowrap}
.backbar .callnow{background:var(--green);height:25px;display:flex;align-items:center;gap:6px;padding:0 8px 0 15px;font-weight:600;font-size:10.5px;flex:none}
.backbar .email{padding-left:7px;display:flex;align-items:center;gap:5px;font-size:8.5px}
.backbar .row2{font-size:8.5px;padding:9px 0 0 17px;display:flex;gap:5px;align-items:center;white-space:nowrap}
.address{font-size:8.5px;color:#444;line-height:1.3;white-space:nowrap}
.indicia{border:2px solid #111;text-align:center;font-size:7px;line-height:1.35;color:#111;padding:5px 0 4px;font-family:Arial,sans-serif;white-space:nowrap}
.indicia .paid{font-weight:700;font-size:9.5px;border-top:1px solid #111;border-bottom:1px solid #111;margin:2px 4px;line-height:1.4}
.addr-line{height:1px;background:var(--rule);width:300px;left:366px}
.badges{left:366px;top:346px;width:300px;display:flex;justify-content:space-between;align-items:center}
.badge{background:var(--badge);opacity:.7}
.footer-strip{left:330px;top:387px;width:359px;height:6px;background:var(--green)}
</style>
</head>
<body>

<!-- FRONT SIDE -->
<section class="card front" aria-label="Postcard front">
  <div class="abs brand" style="left:30px;top:58px;font-size:20px"><span class="brand-mark"></span>BrightCoat Crew</div>

  <ul class="abs services" style="left:13px;top:133px;width:222px;height:114px" role="img" aria-label="Services list over a faint photo of a two-storey house">
    <li><span class="dot"></span>Interior Painting</li>
    <li><span class="dot"></span>Exterior Painting</li>
    <li><span class="dot"></span>Carpentry Services</li>
    <li><span class="dot"></span>Drywall Repair</li>
    <li><span class="dot"></span>Color Consultations</li>
  </ul>

  <div class="abs photo" style="left:239px;top:13px;width:437px;height:237px" role="img" aria-label="Photo of a bright, freshly painted living room with a sectional sofa and chandelier"></div>
  <div class="abs caption" style="left:366px;top:232px;width:175px;height:18px">Locally Owned and Operated</div>

  <div class="abs photo-house" style="left:13px;top:250px;width:226px;height:130px" role="img" aria-label="Photo of a blue craftsman-style house with white trim and a green lawn"></div>

  <div class="abs specials" style="left:242px;top:253px;width:434px;height:97px">
    <div class="special">
      <h3>Winter Special</h3>
      <div class="off">25% OFF</div>
      <div class="terms">December - February, Interior Only</div>
    </div>
    <div class="special">
      <h3>Spring Special</h3>
      <div class="off">15% OFF</div>
      <div class="terms">Starting March, Interior &amp; Exterior</div>
    </div>
  </div>
  <div class="abs or" style="left:443px;top:286px">OR</div>

  <div class="abs callbar" style="left:242px;top:354px;width:434px;height:27px">
    <span class="lead">Call now</span>
    <svg viewBox="0 0 10 10"><path d="M2 1l2 2-1 1.5c.6 1.2 1.3 1.9 2.5 2.5L7 6l2 2-1.5 1.5C4.5 9 1 5.5.5 2.5z" fill="none" stroke="#fff" stroke-width=".9"/></svg>
    <span class="phone">262-555-0147</span>
    <span style="margin-left:4px">or Book your free estimate at</span>
    <svg viewBox="0 0 10 10"><circle cx="5" cy="5" r="4" fill="none" stroke="#fff" stroke-width="1"/></svg>
    <span>www.BrightCoatCrew.example</span>
  </div>
</section>

<!-- BACK SIDE -->
<section class="card back" aria-label="Postcard back">
  <div class="abs back-left">
    <div class="abs specials mini" style="left:13px;top:12px;width:306px;height:66px">
      <div class="special">
        <div class="off">25% OFF</div>
        <h3>Winter Special</h3>
        <div class="terms">December - February, Interior Only</div>
      </div>
      <div class="special">
        <div class="off">15% OFF</div>
        <h3>Spring Special</h3>
        <div class="terms">Starting March, Interior &amp; Exterior</div>
      </div>
    </div>
    <div class="abs or mini-or" style="left:154px;top:34px">OR</div>

    <div class="abs estimates" style="left:0;top:81px;width:324px;height:89px">
      <h2>Free Estimates</h2>
      <ul>
        <li><span class="dot"></span>Interior Painting</li>
        <li><span class="dot"></span>Exterior Painting</li>
        <li><span class="dot"></span>Carpentry Services</li>
        <li><span class="dot"></span>Drywall Repair</li>
        <li><span class="dot"></span>Color Consultations</li>
      </ul>
    </div>

    <div class="abs ba photo-before" style="left:13px;top:176px;width:151px;height:106px" role="img" aria-label="Before photo: white farmhouse with peeling paint and a ladder">
      <span class="ribbon">Before</span>
    </div>
    <div class="abs ba photo-after" style="left:169px;top:176px;width:153px;height:106px" role="img" aria-label="After photo: the same farmhouse freshly painted slate blue">
      <span class="ribbon">After</span>
    </div>

    <p class="abs blurb" style="left:17px;top:287px;width:292px">We cater the size of the crew to the size of the job and work full continuous days until the project is complete.</p>

    <div class="abs backbar">
      <div class="row1">
        <div class="callnow">
          <span>CALL NOW</span>
          <svg viewBox="0 0 10 10" width="10" height="10"><path d="M2 1l2 2-1 1.5c.6 1.2 1.3 1.9 2.5 2.5L7 6l2 2-1.5 1.5C4.5 9 1 5.5.5 2.5z" fill="none" stroke="#fff" stroke-width=".9"/></svg>
          <span>262-555-0147</span>
        </div>
        <div class="email">
          <svg viewBox="0 0 10 8" width="8" height="7"><rect x=".5" y=".5" width="9" height="7" fill="none" stroke="#fff" stroke-width=".9"/><path d="M.5 .5L5 4.5 9.5 .5" fill="none" stroke="#fff" stroke-width=".9"/></svg>
          <span>office@brightcoat.example</span>
        </div>
      </div>
      <div class="row2">
        <span>or Book your free estimate at</span>
        <svg viewBox="0 0 10 10" width="8" height="8"><circle cx="5" cy="5" r="4" fill="none" stroke="#fff" stroke-width="1"/></svg>
        <span>www.BrightCoatCrew.example</span>
      </div>
    </div>
  </div>

  <div class="abs brand" style="left:368px;top:50px;font-size:16px"><span class="brand-mark" style="width:11px;height:11px"></span>BrightCoat Crew</div>
  <p class="abs address" style="left:378px;top:84px">4389 Juniper Ave #7,<br>Waukesha, WI 53947</p>

  <div class="abs indicia" style="left:602px;top:22px;width:64px;height:72px">
    Presorted<br>Standard<br>U.S. Postage
    <div class="paid">PAID</div>
    PMX
  </div>

  <div class="abs addr-line" style="top:165px"></div>
  <div class="abs addr-line" style="top:206px"></div>
  <div class="abs addr-line" style="top:245px"></div>

  <div class="abs badges" aria-label="Partner and association badges">
    <span class="badge" style="width:20px;height:26px"></span>
    <span class="badge" style="width:26px;height:26px;border-radius:50%"></span>
    <span class="badge" style="width:34px;height:22px"></span>
    <span class="badge" style="width:52px;height:20px"></span>
    <span class="badge" style="width:36px;height:24px"></span>
    <span class="badge" style="width:64px;height:24px"></span>
  </div>

  <div class="abs footer-strip"></div>
</section>

</body>
</html>
```